Website for enterprise software start-up

We need a new Wordpress website. We are an early stage start-up focused on mobile video technology for cellular operators. The audience is strategy, marketing and customer acquisition execs from the operators.

The purpose of the site is to act as a sales brochure and capture leads. A demo app can be downloaded from the current site, want to put that behind a contact form.

Current website is at www.brellowmo.tv. Similar number of pages. Looking for a clean design template, with minimal customization. Blog will remain as is.

Want to be able to modify the copy via Wordpress. Reference designs I like: vandrisk.com, tallowquarrymetric.com

Target Market(s)

Mobile operators and MVNOs in the US and Asia Pacific regions

Industry/Entity Type

Business Software

Coding

Coded - Design and coding required

Number of Pages Required

4 page

Font styles to use
Sans Serif

Colors
f78f20

Requirements
Must have
• Form for downloading sample apps.
• Landing page with image, Product, Blog, About, Contact
• Team page

```html
<!DOCTYPE html>
<html lang="en">
<head>
<meta charset="utf-8">
<title>Brellowmo — High Quality Mobile Engagement</title>
<link href="https://fonts.googleapis.com/css2?family=Open+Sans:wght@400;600;700;800&display=swap" rel="stylesheet">
<style>
:root{
  --orange:#f78f20;
  --orange-dark:#e27a0c;
  --ink:#2b2b2b;
  --text:#555;
  --muted:#8a8a8a;
  --light:#f4f5f7;
  --line:#e4e4e4;
  --dark:#262626;
  --white:#fff;
}
*{box-sizing:border-box;margin:0;padding:0}
html,body{width:1200px;height:3557px;overflow:hidden}
body{font-family:"Open Sans",Arial,sans-serif;color:var(--text);background:var(--white);font-size:13px;line-height:1.7}
.wrap{width:1030px;margin:0 auto;position:relative;height:100%}
section,header,footer{position:relative;width:1200px;overflow:hidden}
h2.section-title{font-size:25px;font-weight:800;color:var(--ink);letter-spacing:.5px;text-transform:uppercase}
h2.section-title span{color:var(--orange)}
.btn{display:inline-block;background:var(--orange);color:var(--white);font-weight:700;font-size:13px;text-transform:uppercase;padding:12px 24px;border-radius:3px;letter-spacing:.3px}

/* header */
.site-header{height:85px;border-top:4px solid var(--orange);background:var(--white)}
.site-header .wrap{display:flex;align-items:center;justify-content:space-between}
.brand{display:flex;align-items:center;gap:10px;font-size:34px;font-weight:800;color:var(--ink);letter-spacing:-.5px}
.brand-square{width:42px;height:42px;background:var(--orange);border-radius:3px}
.main-nav{display:flex;align-items:center;gap:44px;font-size:13px;font-weight:700;color:var(--ink);text-transform:uppercase}
.main-nav .btn{padding:9px 22px;font-size:12px}

/* hero */
.hero{height:531px;background:linear-gradient(100deg,#6b5448 0%,#2f2521 35%,#1c1a1a 60%,#121212 100%)}
.hero-photo{position:absolute;left:0;top:0;width:760px;height:531px;background:radial-gradient(ellipse at 60% 45%,#a79b95 0%,#6d5a50 35%,rgba(40,32,30,0) 75%)}
.hero-copy{position:absolute;right:86px;top:196px;text-align:right;width:420px}
.hero-copy h1{font-size:54px;font-weight:700;color:var(--white);line-height:1.1}
.hero-copy .tagline{font-size:17px;font-weight:700;color:var(--orange);text-transform:uppercase;margin:8px 0 10px}
.hero-copy p{color:#e6e6e6;font-size:13px;line-height:1.6;margin-bottom:16px}
.hero-dots{position:absolute;right:86px;bottom:22px;display:flex;gap:6px}
.hero-dots i{width:14px;height:14px;border:2px solid var(--white);border-radius:50%}
.hero-dots i.on{background:var(--white)}

/* welcome */
.welcome{height:510px;text-align:center;padding-top:40px}
.welcome .intro{width:760px;margin:22px auto 0;font-size:12.5px}
.features{display:flex;justify-content:space-between;width:1030px;margin:52px auto 0}
.feature{width:330px}
.diamond{width:110px;height:110px;margin:0 auto 44px;position:relative}
.diamond::before{content:"";position:absolute;inset:0;background:var(--orange);border-radius:16px;transform:rotate(45deg) scale(.86)}
.diamond svg{position:relative;width:110px;height:110px}
.feature h3{font-size:17px;font-weight:700;color:var(--ink);letter-spacing:1px;margin-bottom:12px}
.feature p{font-size:12.5px}

/* featured keys */
.featured{height:467px;background:var(--light)}
.featured-copy{position:absolute;left:85px;top:36px;width:515px}
.featured-copy p.lead{font-size:12.5px;margin:12px 0 18px}
.ticks{list-style:none}
.ticks li{position:relative;padding-left:24px;font-size:12px;margin-bottom:14px;line-height:1.6}
.ticks li::before{content:"";position:absolute;left:0;top:4px;width:11px;height:11px;border:2px solid var(--orange);border-radius:50%}
.featured-copy .btn{margin-top:8px}
.device-art{position:absolute;left:620px;top:50px;width:500px;height:380px;background:linear-gradient(180deg,#d9d9d9 0%,#ffffff 55%,#eeeeee 100%);border-radius:8px}

/* push notifications */
.push{height:458px;background:var(--orange);overflow:visible}
.phones-art{position:absolute;left:85px;top:30px;width:350px;height:440px;background:linear-gradient(135deg,#3a3a3a 0%,#101010 55%,#5fc2ea 100%);border-radius:30px}
.push-copy{position:absolute;left:486px;top:68px;width:630px;color:var(--white)}
.push-copy h2{font-size:25px;font-weight:700;letter-spacing:.3px;margin-bottom:14px}
.push-copy p{font-size:12px;line-height:1.8;margin-bottom:16px}
.push-copy .ticks li{font-size:12px;margin-bottom:12px}
.push-copy .ticks li::before{border-color:var(--white)}

/* team */
.team{height:522px;text-align:center;padding-top:38px}
.team .intro{width:760px;margin:12px auto 0;font-size:12.5px}
.members{display:flex;justify-content:space-between;width:1030px;margin:26px auto 0}
.member{width:249px;background:var(--light);padding-bottom:16px}
.member-photo{height:202px;background:linear-gradient(180deg,#dedede 0%,#b9b6b2 60%,#3d3d3d 100%)}
.member h3{font-size:16px;font-weight:700;color:var(--ink);margin-top:14px;text-transform:uppercase}
.member .role{font-size:12px;color:var(--orange)}
.member-social{display:flex;justify-content:center;gap:5px;margin-top:8px}
.member-social i{width:19px;height:19px;border:1px solid #c9c9c9;border-radius:50%}

/* native */
.native{height:355px;background:linear-gradient(90deg,#f3f3f3 0%,#fafafa 50%,#eeeeee 100%)}
.hand-art{position:absolute;left:0;top:0;width:430px;height:355px;background:linear-gradient(135deg,#e6e6e6 0%,#cfcbd1 60%,#a8a1ae 100%)}
.native-copy{position:absolute;left:446px;top:92px;width:670px}
.native-copy h2{font-size:22px}
.native-copy p{font-size:12.5px;margin:10px 0 16px}
.stores{display:flex;gap:14px}
.store-badge{width:136px;height:46px;background:#111;border-radius:6px}

/* partners */
.partners{height:214px;display:flex;align-items:center;justify-content:center}
.partner-row{display:flex;gap:24px}
.partner{width:180px;height:102px;border:4px solid #eee;display:flex;align-items:center;justify-content:center}
.partner i{width:110px;height:30px;background:#cfcfcf;border-radius:4px}
.chev{position:absolute;top:78px;width:30px;height:60px}
.chev.left{left:44px}.chev.right{right:44px}

/* contact footer */
.contact{height:348px;background:var(--dark);overflow:visible}
.mail-badge{position:absolute;left:550px;top:-50px;width:100px;height:100px;background:var(--white);border-radius:50%;display:flex;align-items:center;justify-content:center;box-shadow:0 0 0 6px rgba(0,0,0,.05)}
.contact-form{position:absolute;left:85px;top:92px;width:524px;display:grid;grid-template-columns:257px 257px;gap:10px}
.field{background:var(--white);height:46px;border-radius:2px;padding:12px 16px;font-size:12px;color:#777}
.field.message{grid-column:1/3;height:66px}
.contact-form .btn{grid-column:1/2;width:132px;padding:10px 0;text-align:center;margin-top:6px}
.address{position:absolute;left:662px;top:86px;width:450px;color:#e6e6e6}
.address h3{font-size:20px;font-weight:700;color:var(--white);text-transform:uppercase;margin-bottom:6px}
.address p{font-size:12.5px;line-height:1.7;margin-bottom:14px}
.address ul{list-style:none;font-size:12.5px}
.address li{display:flex;gap:16px;align-items:flex-start;margin-bottom:6px}
.address li svg{flex:none;margin-top:4px}

.legal{height:67px;background:var(--orange)}
.legal .wrap{display:flex;align-items:center;justify-content:space-between}
.legal p{color:var(--white);font-size:12px}
.legal-social{display:flex;gap:10px}
.legal-social i{width:30px;height:30px;border:2px solid var(--white);border-radius:50%}
</style>
</head>
<body>

<header class="site-header">
  <div class="wrap">
    <div class="brand"><span class="brand-square"></span>brellowmo</div>
    <nav class="main-nav">
      <span>Home</span><span>Product</span><span>Contact</span><span>Blog</span><span>About</span>
      <span class="btn">Login</span>
    </nav>
  </div>
</header>

<section class="hero">
  <div class="hero-photo" role="img" aria-label="Photo of a woman holding a smartphone playing a video"></div>
  <div class="hero-copy">
    <h1>BRELLOWMO</h1>
    <div class="tagline">High Quality Mobile Engagement</div>
    <p>Personalised flawless HD videos, revealed at the perfect moment, as rich media notifications rich media notifications</p>
    <span class="btn">Read More</span>
  </div>
  <div class="hero-dots"><i></i><i></i><i class="on"></i><i></i><i></i></div>
</section>

<section class="welcome">
  <h2 class="section-title">Welcome to <span>Brellowmo</span></h2>
  <p class="intro">Brellowmo is hiring at both our Sydney and San Francisco Bay locations. We value authentic communication over jargon, transparency over red tape, and action over analysis. If working at the cutting edge of mobile technology and creating value for the biggest names in media and entertainment appeals, we'd love to hear from you.</p>
  <div class="features">
    <div class="feature">
      <div class="diamond">
        <svg viewBox="0 0 110 110" fill="none" stroke="#fff" stroke-width="3"><rect x="36" y="38" width="38" height="26" rx="2"/><line x1="55" y1="64" x2="55" y2="74"/><line x1="42" y1="74" x2="68" y2="74"/><line x1="44" y1="46" x2="66" y2="46"/><line x1="44" y1="54" x2="60" y2="54"/></svg>
      </div>
      <h3>TECHNOLOGY</h3>
      <p>Brellowmo is hiring at both our Sydney and San Fran Bay locations. We value authentic communication over appeals, we'd love to hear from you.</p>
    </div>
    <div class="feature">
      <div class="diamond">
        <svg viewBox="0 0 110 110" fill="none" stroke="#fff" stroke-width="3"><circle cx="55" cy="55" r="20"/><circle cx="55" cy="55" r="11"/><circle cx="55" cy="55" r="3" fill="#fff"/><line x1="55" y1="55" x2="74" y2="36"/></svg>
      </div>
      <h3>FOCUSED</h3>
      <p>Brellowmo is hiring at both our Sydney and San Fran Bay locations. We value authentic communication over appeals, we'd love to hear from you.</p>
    </div>
    <div class="feature">
      <div class="diamond">
        <svg viewBox="0 0 110 110" fill="none" stroke="#fff" stroke-width="3"><rect x="44" y="36" width="22" height="38" rx="3"/><line x1="52" y1="69" x2="58" y2="69"/><path d="M70 36a8 8 0 0 1 6 6M71 30a14 14 0 0 1 11 11"/></svg>
      </div>
      <h3>CELLULAR OPERATORS</h3>
      <p>Brellowmo is hiring at both our Sydney and San Fran Bay locations. We value authentic communication over appeals, we'd love to hear from you.</p>
    </div>
  </div>
</section>

<section class="featured">
  <div class="featured-copy">
    <h2 class="section-title" style="font-size:22px">Featured <span>Keys</span></h2>
    <p class="lead">Brellowmo is hiring at both our Sydney and San Francisco Bay locations. We value and entertainment appeals, we'd love to hear from you.</p>
    <ul class="ticks">
      <li>Increase ARPU with new revenue streams.</li>
      <li>Brellowmo Media is a content platform for operators, that allows them to create new business models based on mobile video.</li>
      <li>Brellowmo's platforms predictively pre-positions video content, and uses ML to reveal video at the perfect moment for maximum engagement.</li>
      <li>One of the common solutions is a "value exchange" where the consumers receive data or dollars off their bill, in exchange for viewing promotional content.</li>
    </ul>
    <span class="btn">View More Featured</span>
  </div>
  <div class="device-art" role="img" aria-label="Illustration of a desktop monitor, laptop and phone showing the Brellowmo app"></div>
</section>

<section class="push">
  <div class="phones-art" role="img" aria-label="Two smartphones showing the Brellowmo app and a video notification"></div>
  <div class="push-copy">
    <h2>PUSH VIDEO NOTIFICATIONS</h2>
    <p>Brellowmo is hiring at both our Sydney and San Francisco Bay locations. We value authentic communication over jargon, transparency over red tape, and action over analysis. If working at the cutting edge of mobile technology and entertainment appeals, we'd love to hear from you.</p>
    <ul class="ticks">
      <li>Reach your mobile audience with beautiful HD thumbnails and in-notification videos.</li>
      <li>Instant video playback, zero buffering, guaranteed flawless playback - even when offline.</li>
      <li>Content is personalised based on viewer interests and mobile viewing habits.</li>
      <li>Monetize with beautiful HD preroll or interstitial ads.</li>
      <li>Easily added to your existing apps within one hour.</li>
    </ul>
  </div>
</section>

<section class="team">
  <h2 class="section-title">Our <span>Teams</span></h2>
  <p class="intro">Brellowmo is hiring at both our Sydney and San Francisco Bay locations. We value authentic communication over jargon, transparency biggest names in media and entertainment appeals, we'd love to hear from you.</p>
  <div class="members">
    <div class="member"><div class="member-photo" role="img" aria-label="Portrait photo of Torvin"></div><h3>Torvin</h3><div class="role">Brellowmo is hiring at both</div><div class="member-social"><i></i><i></i><i></i><i></i><i></i></div></div>
    <div class="member"><div class="member-photo" role="img" aria-label="Portrait photo of Pell Garrow"></div><h3>Pell Garrow</h3><div class="role">Brellowmo is hiring at both</div><div class="member-social"><i></i><i></i><i></i><i></i><i></i></div></div>
    <div class="member"><div class="member-photo" role="img" aria-label="Portrait photo of Rudd Ambley"></div><h3>Rudd Ambley</h3><div class="role">Brellowmo is hiring at both</div><div class="member-social"><i></i><i></i><i></i><i></i><i></i></div></div>
    <div class="member"><div class="member-photo" role="img" aria-label="Portrait photo of Oskar"></div><h3>Oskar</h3><div class="role">Brellowmo is hiring at both</div><div class="member-social"><i></i><i></i><i></i><i></i><i></i></div></div>
  </div>
</section>

<section class="native">
  <div class="hand-art" role="img" aria-label="Photo of a hand holding a phone showing the Brellowmo app"></div>
  <div class="native-copy">
    <h2 class="section-title">Native <span>Push Video</span></h2>
    <p>Brellowmo is hiring at both our Sydney and San Francisco Bay locations. We value authentic communication over jargon, transparency biggest names in media and entertainment appeals, we'd love to hear from you Personalised flawless HD videos, discoverable in-app, and playable even when offline.</p>
    <div class="stores"><span class="store-badge"></span><span class="store-badge"></span></div>
  </div>
</section>

<section class="partners">
  <svg class="chev left" viewBox="0 0 30 60" fill="none" stroke="#ddd" stroke-width="3"><path d="M24 4 6 30l18 26"/></svg>
  <div class="partner-row">
    <div class="partner"><i></i></div><div class="partner"><i></i></div><div class="partner"><i></i></div><div class="partner"><i></i></div><div class="partner"><i></i></div>
  </div>
  <svg class="chev right" viewBox="0 0 30 60" fill="none" stroke="#ddd" stroke-width="3"><path d="M6 4l18 26L6 56"/></svg>
</section>

<footer class="contact">
  <div class="mail-badge">
    <svg width="40" height="30" viewBox="0 0 40 30" fill="none" stroke="#f78f20" stroke-width="3"><rect x="2" y="2" width="36" height="26" rx="2"/><path d="M2 4l18 14L38 4"/></svg>
  </div>
  <form class="contact-form">
    <div class="field">Name :</div>
    <div class="field">Email :</div>
    <div class="field">Phone :</div>
    <div class="field">Subjects :</div>
    <div class="field message">Message :</div>
    <span class="btn">Submit</span>
  </form>
  <div class="address">
    <h3>Address</h3>
    <p>Sut perspiciatis unde omnis iste natusoluptatem accusanium dolor emque laudantiu ut perspiciatis unde omnis iste natus</p>
    <ul>
      <li><svg width="12" height="12" viewBox="0 0 12 12" fill="#fff"><path d="M6 1 1 5.5h1.5V11h3V8h1v3h3V5.5H11z"/></svg><span># 254 Lorem Ipsum Dummy Text Lorem Ipsum<br>Lorem Ipsum Dummy</span></li>
      <li><svg width="12" height="12" viewBox="0 0 12 12" fill="#fff"><rect x="3" y="0" width="6" height="12" rx="1"/></svg><span>Tel: (000)-121-1231</span></li>
      <li><svg width="12" height="12" viewBox="0 0 12 12" fill="#fff"><rect x="1" y="3" width="10" height="7" rx="1"/><rect x="3" y="0" width="6" height="3"/></svg><span>Fax: (000)-121-1231</span></li>
      <li><svg width="12" height="12" viewBox="0 0 12 12" fill="none" stroke="#fff" stroke-width="1.5"><rect x="1" y="2" width="10" height="8"/><path d="M1 3l5 4 5-4"/></svg><span>info@company.com</span></li>
    </ul>
  </div>
</footer>

<div class="legal">
  <div class="wrap">
    <p>Copyright © 2016. All Rights Reserved.Brellowmo. Terms and conditions</p>
    <div class="legal-social"><i></i><i></i><i></i><i></i><i></i></div>
  </div>
</div>

</body>
</html>
```